Business Card Design Project

I need a new business card design for my building/development company: Kestrel Ridge Builders.

We specialise in small sub-divisions, multi-story developments and new house builds.
We handle the whole process from concept stage right throught to a fully developed property.
Updates

Target Market(s)

people looking to develop their property and need help. New property buyers

Industry/Entity Type

House

Requirements
Must have
• My logo on both sides:
Side 1: Logo taking up whole side as per old card but with a color/style change.

Side 2: Contact page: include logo but the rest just surprise me!

All contact details will be: (and need to be changable for each employee) I'll inform you of specifics before printing.

Name Surname
Position ie. Managing director
M: insert mobile
E: insert email
P.O. Box 518, Ashwell, Vic, 3094
www.kestrelridgebuilders.com.au

Nice to have
• Colors i'd like: (not necessarily all but this is the basic idea)

Black, blue, grey, silver, white

```html
<!DOCTYPE html>
<html lang="en">
<head>
<meta charset="utf-8">
<title>Kestrel Ridge Builders – Business Card Front</title>
<link rel="stylesheet" href="https://fonts.googleapis.com/css2?family=Arimo:wght@400;700&display=swap">
<style>
  :root {
    --blue-deep: #0b7dd0;
    --blue-mid: #3d9ae0;
    --blue-glow: #e9f3fc;
    --ink: #0a0a0a;
    --white: #ffffff;
    --web-blue: #a9d0f2;
  }
  * { margin: 0; padding: 0; box-sizing: border-box; }
  html, body {
    width: 1200px;
    height: 777px;
    overflow: hidden;
    background: var(--blue-deep);
  }
  .card {
    position: relative;
    width: 1200px;
    height: 777px;
    overflow: hidden;
    background:
      radial-gradient(circle at 680px 290px,
        var(--blue-glow) 0%,
        #9fcbf0 14%,
        var(--blue-mid) 34%,
        var(--blue-deep) 62%);
    font-family: "Arimo", Arial, sans-serif;
    text-align: center;
  }
  .brand-mark {
    position: absolute;
    left: 600px;
    top: 250px;
    width: 160px;
    height: 160px;
    margin-left: -80px;
    border-radius: 50%;
    background: var(--white);
  }
  .company-name {
    position: absolute;
    left: 0;
    right: 0;
    top: 482px;
    font-size: 96px;
    font-weight: 700;
    line-height: 1;
    letter-spacing: -1px;
    color: var(--white);
    white-space: nowrap;
  }
  .tagline {
    position: absolute;
    left: 0;
    right: 0;
    top: 594px;
    font-size: 51px;
    font-weight: 400;
    line-height: 1;
    color: var(--ink);
    white-space: nowrap;
  }
  .website {
    position: absolute;
    left: 0;
    right: 0;
    top: 676px;
    font-size: 31px;
    font-weight: 400;
    line-height: 1;
    letter-spacing: 9px;
    color: var(--web-blue);
    white-space: nowrap;
  }
</style>
</head>
<body>
  <main class="card">
    <div class="brand-mark"></div>
    <h1 class="company-name">Kestrel Ridge Builders</h1>
    <p class="tagline">renovation-construction-development</p>
    <p class="website">www.kestrelridgebuilders.com.au</p>
  </main>
</body>
</html>
```